Rent Kiosks and Tablets

Website for rental kiosks and tablets following the model / style http://www.quellstander.com/. May be the same, with changes in visual identity.
The site should also have an online order system like an e-commerce, which allows payment by credit card and ticket.

The company is called Bolumexa.com and feel free to create/suggest styles of names design.

Target Market(s)

Events, trade shows, marketing companies.

Industry/Entity Type

Credit Card

Font styles to use
Sans Serif

Colors

Designer to choose colors to be used in the design.

```html
<!DOCTYPE html>
<html lang="en">
<head>
<meta charset="utf-8">
<title>Bolumexa — Tablet &amp; Kiosk Rental</title>
<link href="https://fonts.googleapis.com/css2?family=Bree+Serif&family=Open+Sans:wght@400;600;700&display=swap" rel="stylesheet">
<style>
:root{
  --green:#12a21f;
  --top:#2b2b2b;
  --nav:#1f1f1f;
  --footer:#222222;
  --light:#f2f2f2;
  --text:#6b6b6b;
  --white:#ffffff;
  --logo-grey:#6f6f6f;
  --media:#4a4a4a;
}
*{box-sizing:border-box;margin:0;padding:0}
html,body{width:902px;height:1200px;overflow:hidden}
body{position:relative;background:var(--white);font-family:"Open Sans",sans-serif;color:var(--text)}
.abs{position:absolute}
.band{position:absolute;left:0;width:902px}
.topbar{top:0;height:33px;background:var(--top)}
.phone{left:598px;top:9px;color:var(--white);font-weight:600;font-size:11px}
.login{left:685px;top:8px;width:69px;height:19px;background:var(--green);color:var(--white);font-weight:700;font-size:9px;text-align:center;line-height:19px;letter-spacing:.3px}
.navbar{top:33px;height:56px;background:var(--nav)}
.logo{left:144px;top:46px;font-family:"Bree Serif",serif;font-size:27px;color:var(--green);line-height:1}
.nav a{position:absolute;top:55px;color:#e6e6e6;font-size:10px;text-decoration:none}
.hero-title{left:145px;top:136px;font-family:"Bree Serif",serif;font-weight:400;font-size:15.5px;color:var(--green)}
.para{font-size:8.8px;line-height:15.4px;color:var(--text);white-space:nowrap}
.btn{background:var(--green);color:var(--white);font-family:"Bree Serif",serif;font-size:11.5px;text-align:center;line-height:25px;height:25px;width:99px}
.shot{position:absolute;box-shadow:0 6px 14px rgba(0,0,0,.18)}
.tablets{top:327px;height:311px;background:var(--light)}
.section-title{font-family:"Bree Serif",serif;font-weight:400;font-size:15.5px;color:var(--green)}
.platform{position:absolute;top:578px;width:200px;display:flex;justify-content:center;align-items:center;gap:7px;font-weight:600;color:var(--logo-grey)}
.platform i{display:inline-block;width:16px;height:16px;background:var(--logo-grey)}
.media{top:938px;height:59px;background:var(--light)}
.media-name{position:absolute;top:964px;height:20px;line-height:20px;font-weight:600;color:var(--media);white-space:nowrap}
.footer{top:997px;height:203px;background:var(--footer)}
.fhead{top:1025px;color:var(--green);font-weight:600;font-size:9.5px}
.flist{list-style:none;font-size:7.8px;color:#e0e0e0}
.flist li{height:15.4px;line-height:15.4px}
.field{width:142px;height:17px;background:var(--white);border:1px solid #ccc;font-size:7px;color:#aaa;padding-left:8px;line-height:15px}
.subscribe{left:540px;top:1133px;width:62px;height:16px;border-radius:8px;background:var(--green);color:var(--white);font-size:8px;font-weight:600;text-align:center;line-height:16px}
.social{left:666px;width:88px;height:18px}
.social svg{position:absolute;left:0;top:0}
.social span{position:absolute;right:0;top:3px;color:#e0e0e0;font-size:7.8px}
.copy{left:0;width:902px;top:1166px;text-align:center;font-size:7.8px;color:#e0e0e0}
</style>
</head>
<body>

<header>
  <div class="band topbar"></div>
  <div class="abs phone">1-800-555-0148</div>
  <div class="abs login">LOGIN</div>
  <div class="band navbar"></div>
  <div class="abs logo">Bolumexa</div>
  <nav class="nav">
    <a href="#" style="left:360px">Home</a>
    <a href="#" style="left:414px">About Us</a>
    <a href="#" style="left:474px">Services</a>
    <a href="#" style="left:529px">Product</a>
    <a href="#" style="left:586px">Leasing</a>
    <a href="#" style="left:642px">Case Studies</a>
    <a href="#" style="left:720px">Contact</a>
  </nav>
</header>

<section class="hero">
  <h1 class="abs hero-title">Tablet &amp; Kiosk For Rent</h1>
  <p class="abs para" style="left:149px;top:168px">Lorem Ipsum is simply dummy text of the printing and typesetting indus-<br>try. Lorem Ipsum has been the industry's standard dummy text ever<br>since the 1500s, when an unknown printer took a galley of type and<br>scrambled it to make a type specimen book.</p>
  <div class="abs btn" style="left:148px;top:240px">Get Started</div>
  <svg class="abs" style="left:146px;top:283px" width="34" height="16" viewBox="0 0 34 16" aria-label="Slide controls">
    <circle cx="7.5" cy="8" r="7" fill="#555"/>
    <path d="M9 4.5 L5.5 8 L9 11.5" stroke="#fff" stroke-width="1.8" fill="none"/>
    <circle cx="25.5" cy="8" r="7" fill="#555"/>
    <path d="M24 4.5 L27.5 8 L24 11.5" stroke="#fff" stroke-width="1.8" fill="none"/>
  </svg>
  <div class="shot" role="img" aria-label="Free-standing silver touchscreen kiosk with a black screen" style="left:464px;top:100px;width:84px;height:215px;border-radius:8px;background:linear-gradient(180deg,#2a2a2a 0%,#3c3c3c 22%,#e4e4e4 30%,#bdbdbd 60%,#8c8c8c 88%,#3a3a3a 100%)"></div>
  <div class="shot" role="img" aria-label="Black tablet showing a colourful grid of city photos" style="left:560px;top:110px;width:190px;height:195px;border-radius:16px;background:radial-gradient(ellipse at 55% 45%,#4f6aa0 0%,#7a5a48 35%,#2e3446 62%,#141414 80%)"></div>
</section>

<section class="band tablets"></section>
<h2 class="abs section-title" style="left:0;width:902px;top:338px;text-align:center">Tablet</h2>
<div class="shot" role="img" aria-label="Black tablet running a dashboard app with green charts" style="left:166px;top:391px;width:140px;height:107px;border-radius:5px;background:radial-gradient(ellipse at 50% 55%,#3d4a3a 0%,#262a26 55%,#0d0d0d 85%)"></div>
<div class="shot" role="img" aria-label="Tablet with a blue home screen and large clock" style="left:370px;top:394px;width:147px;height:104px;border-radius:10px;background:radial-gradient(ellipse at 50% 50%,#2f86de 0%,#1a4fa8 45%,#102a5c 70%,#1c1c1c 88%)"></div>
<div class="shot" role="img" aria-label="Tablet with a tiled purple start screen" style="left:575px;top:391px;width:154px;height:107px;border-radius:5px;background:radial-gradient(ellipse at 50% 50%,#8a4ea8 0%,#5a2a80 45%,#3a1a56 70%,#151515 88%)"></div>
<p class="abs para" style="left:150px;top:506px">Lorem Ipsum is simply dummy text of the<br>printing and typesetting industry. Lorem Ipsum<br>has been the industry's</p>
<p class="abs para" style="left:354px;top:506px">Lorem Ipsum is simply dummy text of the<br>printing and typesetting industry. Lorem Ipsum<br>has been the industry's</p>
<p class="abs para" style="left:562px;top:506px">Lorem Ipsum is simply dummy text of the<br>printing and typesetting industry. Lorem Ipsum<br>has been the industry's</p>
<div class="platform" style="left:125px;font-size:24px">Slate OS</div>
<div class="platform" style="left:342px;font-size:18px"><i></i>Andeva</div>
<div class="platform" style="left:566px;font-size:20px"><i></i>Panes 8</div>

<section class="kiosks">
  <div class="shot" role="img" aria-label="Silver kiosk with angled touchscreen" style="left:150px;top:672px;width:102px;height:240px;border-radius:10px 10px 6px 6px;background:linear-gradient(180deg,#8a8f9a 0%,#3e4552 14%,#c8ccd4 22%,#e9ebef 55%,#a9adb6 100%)"></div>
  <div class="shot" role="img" aria-label="Slim white kiosk with a map display" style="left:275px;top:702px;width:55px;height:180px;border-radius:6px;background:linear-gradient(180deg,#e6e8ec 0%,#2aa0c8 10%,#7cc6a0 30%,#dfe2e7 45%,#f3f4f6 80%,#b7bac1 100%)"></div>
  <div class="shot" role="img" aria-label="Curved silver kiosk with a gold screen" style="left:352px;top:674px;width:94px;height:220px;border-radius:8px;background:linear-gradient(180deg,#d8dbe1 0%,#b89020 10%,#8a6a18 22%,#e4e6ea 32%,#cdd0d6 70%,#a5a8af 100%)"></div>
  <h2 class="abs section-title" style="left:474px;top:656px;font-size:17px">Kiosks</h2>
  <p class="abs para" style="left:474px;top:694px">Lorem Ipsum is simply dummy text of the printing and type-<br>setting industry. Lorem Ipsum has been the industry's stand-<br>ard dummy text ever since the 1500s, when an unknown<br>printer took a galley of type and scrambled it to make a type<br>specimen book.</p>
  <p class="abs para" style="left:474px;top:787px">Sed ut perspiciatis unde omnis iste natus error sit volup-<br>tatem accusantium doloremque laudantium, totam rem<br>aperiam, eaque ipsa quae ab illo inventore veritatis et quasi<br>architecto beatae vitae dicta sunt explicabo. Nemo enim<br>ipsam voluptatem quia voluptas sit aspernatur aut odit aut<br>fugit, sed quia consequuntur magni dolores eos .</p>
  <div class="abs btn" style="left:473px;top:892px">View More</div>
</section>

<section class="band media"></section>
<div class="media-names">
  <span class="media-name" style="left:172px;font-size:8.5px">Westcoast Trade Journal</span>
  <span class="media-name" style="left:274px;font-size:15px">Marlow</span>
  <span class="media-name" style="left:340px;font-size:9px">Channel 9</span>
  <span class="media-name" style="left:403px;font-size:9px;letter-spacing:1px">VENTURE LEDGER</span>
  <span class="media-name" style="left:532px;font-size:11px">ByteWire</span>
  <span class="media-name" style="left:629px;font-size:12.5px">Harbor City Times</span>
</div>

<footer>
  <div class="band footer"></div>
  <h3 class="abs fhead" style="left:149px">Quick Links</h3>
  <h3 class="abs fhead" style="left:304px">Support Links</h3>
  <h3 class="abs fhead" style="left:460px">Newsletter SignUp</h3>
  <h3 class="abs fhead" style="left:665px">Connect With Us</h3>
  <ul class="abs flist" style="left:150px;top:1049px">
    <li>Home</li><li>About Us</li><li>Services</li><li>Product</li><li>Leasing</li><li>Case Studies</li><li>Contact</li>
  </ul>
  <ul class="abs flist" style="left:304px;top:1049px">
    <li>Legal Notice</li><li>Privacy Policy</li><li>Terms &amp; Conditions</li><li>Help</li>
  </ul>
  <p class="abs" style="left:460px;top:1046px;width:160px;font-size:7.8px;line-height:13px;color:#e0e0e0">Sign-up for our daily emails by entering your information below:</p>
  <div class="abs field" style="left:460px;top:1082px">Name</div>
  <div class="abs field" style="left:460px;top:1109px">Enter Your E-Mail ID</div>
  <div class="abs subscribe">Subscribe</div>
  <div class="abs social" style="top:1049px"><svg width="18" height="18"><circle cx="9" cy="9" r="9" fill="#fff"/></svg><span>Chirply</span></div>
  <div class="abs social" style="top:1073px"><svg width="18" height="18"><circle cx="9" cy="9" r="9" fill="#fff"/></svg><span>Circlebook</span></div>
  <div class="abs social" style="top:1097px"><svg width="18" height="18"><circle cx="9" cy="9" r="9" fill="#fff"/></svg><span>WorkLink</span></div>
  <p class="abs copy">Copyright ©2013 Company Name - All rights reserved</p>
</footer>

</body>
</html>
```